Amber Hollow Productions

I need a business card design for a new freelance film production company using or incorporating the logo:
I want the card to be creative, minimal, yet professional. Feel free to use a variety of different shapes and sizes/ textures for the card.

Industry/Entity Type

Film Production

```html
<!DOCTYPE html>
<html lang="en">
<head>
<meta charset="utf-8">
<title>Amber Hollow Productions – Business Card</title>
<link rel="stylesheet" href="https://fonts.googleapis.com/css2?family=Jost:wght@400;500&display=swap">
<style>
  :root {
    --backdrop: #1d1d1e;
    --card-edge: #ffffff;
    --card-face: #e9e9eb;
    --brand-blue: #1456a6;
    --ink-dark: #3a3a3c;
    --ink-light: #ffffff;
    --reel-grey: #a9abb0;
    --reel-shade: #7d8087;
  }
  * { margin: 0; padding: 0; box-sizing: border-box; }
  html, body {
    width: 1200px;
    height: 750px;
    overflow: hidden;
    background: var(--backdrop);
  }
  body {
    display: flex;
    align-items: center;
    justify-content: center;
    font-family: "Jost", "Futura", sans-serif;
  }
  .business-card {
    position: relative;
    width: 900px;
    height: 540px;
    border-radius: 40px;
    background: var(--card-edge);
    padding: 14px;
    box-shadow: 0 20px 50px rgba(0, 0, 0, 0.45);
  }
  .card-face {
    position: relative;
    width: 100%;
    height: 100%;
    border-radius: 28px;
    background: var(--card-face);
    overflow: hidden;
  }
  .holder {
    position: absolute;
    left: 56px;
    top: 96px;
    font-size: 30px;
    font-weight: 400;
    color: var(--ink-dark);
    letter-spacing: 0.2px;
  }
  .holder-name { color: var(--brand-blue); }
  .holder-sep { margin: 0 6px; }
  .brand-name {
    position: absolute;
    right: 70px;
    top: 150px;
    text-align: center;
    font-weight: 400;
    color: var(--brand-blue);
  }
  .brand-title {
    display: block;
    font-size: 52px;
    line-height: 1;
    letter-spacing: 1px;
  }
  .brand-sub {
    display: block;
    margin-top: 6px;
    font-size: 19px;
    letter-spacing: 9px;
  }
  .reel-art {
    position: absolute;
    left: 40px;
    top: 250px;
    width: 86px;
    height: 86px;
    border-radius: 50%;
    background: radial-gradient(circle at 40% 40%, var(--reel-grey), var(--reel-shade));
  }
  .contact-band {
    position: absolute;
    left: 0;
    right: 0;
    bottom: 0;
    height: 208px;
    background: var(--brand-blue);
    color: var(--ink-light);
  }
  .contact-lines {
    position: absolute;
    left: 56px;
    top: 78px;
    font-size: 20px;
    line-height: 1.3;
    font-weight: 400;
  }
</style>
</head>
<body>
  <article class="business-card">
    <div class="card-face">
      <p class="holder">
        <span class="holder-name">Daniel Reyes</span><span class="holder-sep">|</span><span class="holder-role">Director</span>
      </p>

      <h1 class="brand-name">
        <span class="brand-title">AMBER HOLLOW</span>
        <span class="brand-sub">PRODUCTIONS</span>
      </h1>

      <footer class="contact-band">
        <address class="contact-lines" style="font-style: normal;">
          <span>412 Linden Avenue | Maple Falls, OR. 97301</span><br>
          <span>P: (503) 555-0142 | studio@amberhollow.com</span>
        </address>
      </footer>

      <div class="reel-art" role="img" aria-label="Small grey film reel illustration resting on the blue band"></div>
    </div>
  </article>
</body>
</html>
```